Commercial Real Estate Company Needs Website Redesign

Velmarco is a commercial real estate firm that is based in San Diego, but has offices and properties across the U.S. The current website was completed almost 3 years ago and is need of a refresh. We will rework the existing Wordpress CMS system, but require a new design. We have a great programmer who can take the design into wordpress. I need a design template for each page types, There are are approximately 20 pages for each section of our site. There are 4 Sections: Corporate, Hospitality, Commercial/Residential, and Receiver/Bankruptcy. See attached creative brief for the initial pages we would like drafted.

Industry/Entity Type

Real Estate

```html
<!DOCTYPE html>
<html lang="en">
<head>
<meta charset="utf-8">
<title>Velmarco Hospitality</title>
<link href="https://fonts.googleapis.com/css2?family=Arimo:wght@400;700&display=swap" rel="stylesheet">
<style>
  :root{
    --navy-deep:#0a1630;
    --navy:#10223f;
    --navy-line:#2a4a86;
    --blue-btn:#1d4680;
    --blue-text:#2b5ea8;
    --orange:#fbaa35;
    --orange-dark:#f0901c;
    --white:#ffffff;
    --light:#e4e9f1;
    --field:#f4f4f4;
    --field-text:#8a8a8a;
    --ink:#162a4a;
    --foot-text:#555d68;
  }
  *{box-sizing:border-box;margin:0;padding:0}
  html,body{width:1132px;height:1200px;overflow:hidden}
  body{font-family:"Arimo",Arial,sans-serif;background:var(--navy);position:relative}
  .wrap{position:absolute;left:151px;width:830px}

  .topbar{position:absolute;top:0;left:0;width:1132px;height:23px;background:var(--navy-deep)}
  .topbar .contact{position:absolute;right:36px;top:4px;display:flex;align-items:center;gap:8px;color:var(--white);font-weight:700;font-size:12px}
  .topbar .social{width:13px;height:13px;background:var(--white);border-radius:2px}

  .header{position:absolute;top:23px;left:0;width:1132px;height:89px;background:var(--navy)}
  .brand{position:absolute;left:151px;top:32px;display:flex;align-items:center;gap:8px;color:var(--white);font-weight:700;font-size:24px;letter-spacing:0.5px}
  .brand .mark{width:26px;height:26px;border-radius:50%;background:var(--orange)}
  .nav{position:absolute;left:585px;top:31px;width:396px;height:48px;border-bottom:1px solid var(--navy-line);display:flex}
  .nav a{display:block;color:var(--white);text-decoration:none;font-size:11.5px;padding:0 0 0 0;height:47px;line-height:14px}
  .nav a.active{color:var(--orange);border-bottom:2px solid var(--orange);width:78px;text-align:center}
  .nav a:nth-child(2){margin-left:24px}
  .nav a:nth-child(3){margin-left:30px}
  .nav a:nth-child(4){margin-left:30px}

  .hero{position:absolute;top:112px;left:0;width:1132px;height:408px;background:linear-gradient(100deg,#c9d3d6 0%,#8c9aa6 30%,#4d6178 50%,#b7b2ad 72%,#d6dadb 100%)}
  .enquiry{position:absolute;left:151px;top:35px;width:313px;height:342px;background:var(--orange);border:3px solid var(--orange-dark)}
  .enquiry .ribbon{position:absolute;left:-8px;top:16px;width:292px;height:33px;background:linear-gradient(#ffffff,#e2e2e2);clip-path:polygon(0 0,96% 0,100% 50%,96% 100%,0 100%);font-weight:700;font-size:16px;color:var(--ink);line-height:33px;padding-left:34px}
  .enquiry .field{position:absolute;left:23px;width:262px;height:30px;background:var(--field);border:1px solid #e8c48e;font-size:11px;font-weight:700;color:var(--field-text);padding:9px 11px 0}
  .enquiry .select .arrow{position:absolute;right:0;top:0;width:30px;height:28px;background:var(--blue-btn)}
  .enquiry .select svg{position:absolute;left:10px;top:11px}
  .enquiry .textarea{height:68px}
  .enquiry .send{position:absolute;left:23px;top:293px;width:262px;height:30px;background:var(--blue-btn);color:var(--white);font-weight:700;font-size:11.5px;text-align:center;line-height:30px}

  .consult{position:absolute;left:493px;top:283px;width:472px;height:94px;background:rgba(255,255,255,0.9);text-align:center}
  .consult h2{font-size:16.5px;color:var(--ink);margin-top:13px}
  .consult p{font-size:18px;color:var(--blue-text);margin-top:3px}
  .consult .phone{font-size:24px;font-weight:700;color:var(--ink);margin-top:4px}

  .welcome{top:542px;text-align:center}
  .welcome h1{font-size:20px;color:var(--white)}
  .welcome h1 span{color:var(--orange)}
  .welcome p{margin-top:12px;font-size:11.5px;line-height:18.2px;color:var(--light);text-align:justify}

  .card{position:absolute;top:703px;width:256px}
  .card .photo{width:256px;height:108px}
  .card h3{margin-top:14px;font-size:15px;color:var(--white)}
  .card p{margin-top:6px;font-size:11.5px;line-height:16.6px;color:var(--light)}
  .card .more{position:absolute;top:226px;left:0;width:94px;height:28px;background:var(--orange);color:var(--ink);font-weight:700;font-size:12px;text-align:center;line-height:28px}

  .footer{position:absolute;top:1013px;left:0;width:1132px;height:156px;background:#f7f8f9}
  .footer h4{font-size:15px;color:var(--orange);font-weight:700}
  .col{position:absolute;top:24px}
  .links{left:210px}
  .links ul{list-style:none;position:absolute;top:26px;font-size:10.5px;color:var(--foot-text);line-height:19px;width:110px}
  .links ul.second{left:115px}
  .divider{position:absolute;top:24px;width:1px;height:108px;background:var(--orange)}
  .contact-info{left:479px}
  .contact-info li{list-style:none;font-size:10.5px;color:var(--foot-text);display:flex;align-items:center;gap:7px;height:19px}
  .contact-info ul{margin-top:11px}
  .subscribe{left:710px;width:260px}
  .subscribe .row{display:flex;gap:6px;margin-top:10px}
  .subscribe .email{width:164px;height:30px;border:1px solid #d8d8d8;background:var(--white);font-size:10.5px;color:#999;padding:9px 10px 0}
  .subscribe .submit{width:78px;height:30px;background:var(--orange);font-weight:700;font-size:12px;color:var(--ink);text-align:center;line-height:30px}
  .subscribe p{font-size:10.5px;color:var(--foot-text);margin-top:9px}
  .subscribe .icons{display:flex;gap:10px;margin-top:8px}
  .subscribe .icons span{width:15px;height:15px;background:var(--orange);border-radius:2px}

  .copyright{position:absolute;top:1169px;left:0;width:1132px;height:31px;background:var(--orange);color:var(--white);font-size:11px;text-align:center;line-height:31px}
</style>
</head>
<body>

<div class="topbar">
  <div class="contact">
    <svg width="12" height="12" viewBox="0 0 24 24"><path fill="#fff" d="M6.6 10.8c1.4 2.8 3.8 5.1 6.6 6.6l2.2-2.2c.3-.3.7-.4 1-.2 1.1.4 2.3.6 3.6.6.6 0 1 .4 1 1V20c0 .6-.4 1-1 1C10.6 21 3 13.4 3 4c0-.6.4-1 1-1h3.5c.6 0 1 .4 1 1 0 1.3.2 2.5.6 3.6.1.3 0 .7-.2 1z"/></svg>
    <span>555 - 310 - 4782</span>
    <span class="social"></span><span class="social"></span><span class="social"></span>
  </div>
</div>

<header class="header">
  <div class="brand"><span class="mark"></span>Velmarco Hospitality</div>
  <nav class="nav">
    <a class="active" href="#">VELMARCO HOME</a>
    <a href="#">WHO WE ARE</a>
    <a href="#">WHAT WE DO</a>
    <a href="#">WHAT WE'VE DONE</a>
  </nav>
</header>

<section class="hero" role="img" aria-label="Businessman holding a sketch of city buildings in his open hand">
  <div class="enquiry">
    <div class="ribbon">GET IN TOUCH</div>
    <div class="field" style="top:66px">NAME</div>
    <div class="field" style="top:104px">EMAIL</div>
    <div class="field" style="top:142px">PHONE</div>
    <div class="field select" style="top:180px">SUBJECT OF ENQUIRY
      <span class="arrow"><svg width="9" height="5" viewBox="0 0 9 5"><path d="M0 0h9L4.5 5z" fill="#fff"/></svg></span>
    </div>
    <div class="field textarea" style="top:218px">MESSAGE/COMMENTS</div>
    <div class="send">SEND TO EXPERT</div>
  </div>
  <div class="consult">
    <h2>CALL FOR A FREE CONSULTATION</h2>
    <p>Let us put our expertise to work for you.</p>
    <div class="phone">555-310-4782</div>
  </div>
</section>

<section class="wrap welcome">
  <h1><span>WELCOME TO</span> VELMARCO HOSPITALITY</h1>
  <p>Lorem ipsum dolor sit amet, consectetur adipiscing elit. Phasellus a facilisis diam. Vivamus et purus sit amet quam adipiscing mattis vitae non ligula. Duis elementum at ligula id tincidunt. Fusce aliquet tortor non ullamcorper pharetra. Ut suscipit nulla quam, cursus laoreet libero eleifend nec. Nullam sollicitudin condimentum pulvinar. Proin in libero bibendum, iaculis augue eget, tincidunt nisi. Donec fringilla volutpat eros ac suscipit. Nunc pellentesque molestie augue, id iaculis lacus viverra vitae. Maecenas tincidunt, ligula sed mollis blandit, elit lorem molestie mi, faucibus gravida risus dui in tellus. Suspendisse quis velit non urna iaculis aliquam eget nec lectus.</p>
</section>

<article class="card" style="left:151px">
  <div class="photo" role="img" aria-label="Hotel bedroom with white bed and wooden floor" style="background:linear-gradient(#c8b9a6,#e9e4dc 55%,#7a3f22)"></div>
  <h3>FOR OWNERS</h3>
  <p>Lorem ipsum dolor sit amet, consectetur adipiscing elit. Phasellus a facilisis diam. Vivamus et purus sit amet quam adipiscing mattis vitae non ligula. Duis elementum at ligula id tincidunt.</p>
  <div class="more">READ MORE</div>
</article>
<article class="card" style="left:437px">
  <div class="photo" role="img" aria-label="Agent showing an empty home to a couple" style="background:linear-gradient(90deg,#6b5a4a,#cfc4b4 55%,#e6dccb)"></div>
  <h3>FOR BUYERS / DEVELOPERS</h3>
  <p>Lorem ipsum dolor sit amet, consectetur adipiscing elit. Phasellus a facilisis diam. Vivamus et purus sit amet quam adipiscing mattis vitae non ligula. Duis elementum at ligula id tincidunt.</p>
  <div class="more">READ MORE</div>
</article>
<article class="card" style="left:724px">
  <div class="photo" role="img" aria-label="Couple standing in front of a yellow house" style="background:linear-gradient(90deg,#d8c24a,#e8d86a 50%,#c9b98f)"></div>
  <h3>FOR LENDERS</h3>
  <p>Lorem ipsum dolor sit amet, consectetur adipiscing elit. Phasellus a facilisis diam. Vivamus et purus sit amet quam adipiscing mattis vitae non ligula. Duis elementum at ligula id tincidunt.</p>
  <div class="more">READ MORE</div>
</article>

<footer class="footer">
  <div class="col links">
    <h4>Useful Links</h4>
    <ul><li>Home</li><li>About Us</li><li>News</li><li>Privacy Polic</li></ul>
    <ul class="second"><li>Our Company</li><li>Terms &amp; Conditions</li><li>Our Work</li><li>Contact Us</li></ul>
  </div>
  <div class="divider" style="left:446px"></div>
  <div class="col contact-info">
    <h4>Contact Info</h4>
    <ul>
      <li><svg width="10" height="13" viewBox="0 0 10 13"><path d="M5 0a5 5 0 0 1 5 5c0 3.5-5 8-5 8S0 8.5 0 5a5 5 0 0 1 5-5z" fill="#fbaa35"/><circle cx="5" cy="5" r="2" fill="#fff"/></svg>418 Harbor View Ave, Tampa, FL 33602</li>
      <li><svg width="12" height="10" viewBox="0 0 12 10"><rect x="0" y="0" width="12" height="4" rx="2" fill="#fbaa35"/><rect x="2" y="4" width="8" height="6" fill="#fbaa35"/></svg>555-310-4782</li>
      <li><svg width="12" height="9" viewBox="0 0 12 9"><rect width="12" height="9" fill="#fbaa35"/><path d="M0 0l6 5 6-5" stroke="#fff" fill="none"/></svg>info@velmarcohospitality.com</li>
    </ul>
  </div>
  <div class="divider" style="left:681px"></div>
  <div class="col subscribe">
    <h4>Subscribe to our NewsLetter</h4>
    <div class="row"><div class="email">Enter your Email Id</div><div class="submit">SUBMIT</div></div>
    <p>You can also follow us on social networking websites</p>
    <div class="icons"><span></span><span></span><span></span></div>
  </div>
</footer>

<div class="copyright">Copyright 2014 by Velmarco Hospitality. - All Rights Reserved</div>

</body>
</html>
```